Bright Willow Wellness
Heal your Body Mind and Spirit
Bright Willow Wellness - Health
Creative Brief
Professional
Melora T. Grant, MSW, LSW
Health Consultant and Spiritual Counselor
Certifications: Feeling Map Form Key Spiritual Counseling
melora@brightwillowwellness.example
www.brightwillowwellness.example
Next appointment: _____________________________________
guest guest
where is the logo
mgrant417 mgrant417
Designers: Please only design for business cards, not stationary. Thanks...

```html
<!DOCTYPE html>
<html lang="en">
<head>
<meta charset="utf-8">
<title>Bright Willow Wellness – Business Card</title>
<link rel="stylesheet" href="https://fonts.googleapis.com/css2?family=Cinzel:wght@600&family=Crimson+Text:ital,wght@1,700&family=Questrial&display=swap">
<style>
  :root {
    --backdrop: #2b2b2d;
    --card: #ffffff;
    --teal: #2a7f9e;
    --teal-deep: #1d6a8a;
    --navy: #17355c;
    --ink: #3a3a3a;
    --rule: #7a7a7a;
    --faint: #e3eef3;
  }
  * { box-sizing: border-box; margin: 0; padding: 0; }
  html, body { width: 1200px; height: 901px; overflow: hidden; }
  body {
    background: var(--backdrop);
    font-family: "Questrial", "Century Gothic", sans-serif;
    position: relative;
  }
  .card {
    position: absolute;
    top: 296px;
    width: 540px;
    height: 309px;
    background: var(--card);
    border-radius: 14px;
    overflow: hidden;
    box-shadow: 0 10px 30px rgba(0,0,0,.45);
  }
  /* ---------- appointment side ---------- */
  .card--back { left: 40px; color: var(--ink); font-size: 14px; }
  .card--back .faint-mark {
    position: absolute; left: 195px; top: 40px;
    width: 140px; height: 140px; border-radius: 50%;
    background: var(--faint);
  }
  .line { position: absolute; height: 1px; background: var(--rule); }
  .appt-label { position: absolute; left: 30px; top: 68px; }
  .days { position: absolute; left: 30px; top: 96px; display: flex; gap: 16px; }
  .day { display: flex; align-items: center; gap: 6px; }
  .box { width: 18px; height: 18px; border: 1.5px solid var(--ink); display: inline-block; }
  .date-row { position: absolute; left: 30px; top: 176px; }
  .at { position: absolute; left: 338px; top: 176px; }
  .ampm { position: absolute; left: 470px; top: 150px; font-size: 13px; line-height: 1.3; }
  .certs { position: absolute; left: 90px; top: 240px; font-size: 12.5px; white-space: nowrap; }
  /* ---------- front side ---------- */
  .card--front { left: 620px; }
  .card--front svg.waves { position: absolute; inset: 0; }
  .brand { position: absolute; left: 28px; top: 36px; display: flex; align-items: center; gap: 10px; }
  .brand-dot { width: 42px; height: 42px; border-radius: 50%; background: var(--teal-deep); }
  .brand-name {
    font-family: "Cinzel", "Times New Roman", serif; font-weight: 600;
    font-size: 22px; color: var(--teal-deep); letter-spacing: .5px;
  }
  .tagline {
    position: absolute; left: 80px; top: 72px;
    font-family: "Crimson Text", Georgia, serif; font-style: italic; font-weight: 700;
    font-size: 15px; color: var(--teal-deep);
  }
  .contact { position: absolute; right: 26px; top: 182px; color: #fff; text-align: left; width: 250px; }
  .person-name { font-size: 19px; }
  .person-role { font-size: 12px; margin-top: 2px; }
  .contact-list { list-style: none; margin-top: 14px; font-size: 12px; line-height: 1.45; }
  .contact-list li { display: flex; align-items: center; gap: 7px; }
  .contact-list svg { width: 11px; height: 11px; flex: none; }
</style>
</head>
<body>

<section class="card card--back" aria-label="Appointment card">
  <div class="faint-mark" role="img" aria-label="Faint brand mark"></div>
  <div class="line" style="left:30px; right:30px; top:46px;"></div>
  <p class="appt-label">Your Next Appointment</p>
  <div class="line" style="left:200px; right:30px; top:84px;"></div>
  <div class="days">
    <span class="day"><span class="box"></span>Mon</span>
    <span class="day"><span class="box"></span>Tue</span>
    <span class="day"><span class="box"></span>Wed</span>
    <span class="day"><span class="box"></span>Thu</span>
    <span class="day"><span class="box"></span>Fri</span>
    <span class="day"><span class="box"></span>Sat</span>
  </div>
  <p class="date-row">Date:</p>
  <div class="line" style="left:72px; width:258px; top:192px;"></div>
  <p class="at">AT</p>
  <div class="line" style="left:362px; width:100px; top:192px;"></div>
  <p class="ampm">AM<br>PM</p>
  <div class="line" style="left:30px; width:52px; top:250px;"></div>
  <p class="certs">Certifications: Feeling Map | Form Key | Spiritual Counseling</p>
</section>

<section class="card card--front" aria-label="Business card front">
  <svg class="waves" viewBox="0 0 540 309" preserveAspectRatio="none" aria-hidden="true">
    <path d="M0 150 C120 175 260 185 540 118 L540 309 L0 309 Z" fill="var(--navy)"/>
    <path d="M0 162 C130 190 280 196 540 132 L540 309 L0 309 Z" fill="#ffffff"/>
    <path d="M0 170 C140 200 290 204 540 142 L540 309 L0 309 Z" fill="var(--navy)"/>
    <path d="M0 182 C150 212 300 212 540 156 L540 309 L0 309 Z" fill="var(--teal)"/>
  </svg>
  <div class="brand">
    <span class="brand-dot"></span>
    <span class="brand-name">BRIGHT WILLOW WELLNESS</span>
  </div>
  <p class="tagline">Achieve balanced health and well-being</p>
  <div class="contact">
    <p class="person-name">Melora T. Grant, MSW, LSW</p>
    <p class="person-role">Health Consultant and Spiritual Counselor</p>
    <ul class="contact-list">
      <li><svg viewBox="0 0 12 12"><path d="M2 1h3l1 3-1.5 1a6 6 0 0 0 2.5 2.5L8 6l3 1v3c0 1-1 1-1 1A9 9 0 0 1 1 2s0-1 1-1z" fill="#fff"/></svg>555.014.0372</li>
      <li><svg viewBox="0 0 12 12"><rect x="1" y="2.5" width="10" height="7" fill="none" stroke="#fff"/><path d="M1 2.5l5 4 5-4" fill="none" stroke="#fff"/></svg>melora@brightwillowwellness.example</li>
      <li><svg viewBox="0 0 12 12"><circle cx="6" cy="6" r="5" fill="none" stroke="#fff"/><path d="M1 6h10M6 1c-2.5 3-2.5 7 0 10M6 1c2.5 3 2.5 7 0 10" fill="none" stroke="#fff" stroke-width=".8"/></svg>www.brightwillowwellness.example</li>
    </ul>
  </div>
</section>

</body>
</html>
```